WordPress Responsive Website Design & Build

We are looking for a Meridian Child Theme WordPress website. It must be a responsive design - would prefer to see desktop and mobile views of mockup.
Logo supplied.

The site will consist of just a few pages external of the TORVAK store ( which bolts on as a WordPress Plugin and fills the body area of one specific page.

We will pay for and install the bolt on TORVAK store after the site is built.
Looking for a fresh, bright homepage that has some feature areas promoting items from within the store as well as other parts of the website ( blog etc). These homepage areas/sliders will be updated manually so need to be easy to use.
Also would like to see an interior page (Main body 2/3 - Sidebar 1/3 layout for other content pages.

Color palette should come from the logo with any accent colors the designer feels need to be added.

The website is called bramble-nook.ca and will be a hobby job for a stay-at-home mom of 4 kids looking to sell items her kids have outgrown or no longer use. Everything from boys and girls clothing to toys, bikes, piggy banks etc.

We are asking for design mockups of a homepage and an interior page as proofs.
At that point we can have some back and forth on how the areas would need to function. Once, accepted you will also build out those proofs into a responsive Wordpress website.

We can provide a demo hosting environment, install WordPress and Meridian as well as supply you with WordPress admin and ftp access to complete the build portion of this task - or you can provide this all and we can simply migrate to our hosting once the project is complete.

This is a one-off project however - we are looking for an ongoing supplier of similar services. So keep that in mind as you provide service and process. We want to work towards the simplest method and procedures possible in order to establish an ongoing relationship with a designer and provide them with ongoing sporadic design and coding work.

Please advise if you need anymore information.
Updates

Please checkout TORVAK to get a better idea of how this store functions. Here are some not so great showcase stores. https://www.torvak-example.com/showcase Here are some other WordPress websites using TORVAK. https://plumwhistle-example.com/ https://rovo-shop-example.ca/

Target Market(s)

moms ( and some dads) who are either frugal and want good stuff at less-than-new prices or living on a budget. They have one or more kids and live on the prairies of Saskatchewan.

Industry/Entity Type

Clothing

Coding

Coded - Design and coding required

Number of Pages Required

2 page

Font styles to use
Serif
Sans Serif

Colors

Designer to choose colors to be used in the design.

Requirements
Must have
• responsive code
• built on WordPress
• colorful, tight well-thought out design
• feature areas on homepage to feature items in store (ideas are clearance items, newest items, seasonal items etc)
• easily editable images and text - use plugins over html coding in widgets please.
Nice to have
• Prefer that it uses the Meridian Framework
• homepage and interior page proofs - nice to see both a desktop and mobile version of each
Should not have
• Not be built on some non-transferable tool like QuillPatterns
• Not have a bunch of extraneous design elements that make it feel busy
• Not be too sparse and plain either

```html
<!DOCTYPE html>
<html lang="en">
<head>
<meta charset="utf-8">
<title>Bramble-Nook.ca – Home</title>
<link href="https://fonts.googleapis.com/css2?family=Montserrat:wght@400;500;600;700&family=Open+Sans:ital,wght@0,400;0,600;0,700;1,400&family=Fredoka:wght@500&display=swap" rel="stylesheet">
<style>
:root{
  --pink:#e8476a;
  --pink-dark:#d93a5c;
  --blue:#1fa6dd;
  --blue-dark:#1592c8;
  --green:#c5d82e;
  --green-soft:#eef5dc;
  --ink:#222;
  --grey:#666;
  --white:#fff;
}
*{box-sizing:border-box;margin:0;padding:0}
html,body{width:1200px;height:3255px;overflow:hidden;background:#fff}
body{font-family:"Open Sans",Arial,sans-serif;color:var(--ink)}
.page{position:relative;width:1200px;height:3255px;overflow:hidden}
.abs{position:absolute}

/* top bar */
.topbar{left:0;top:0;width:1200px;height:38px;background:var(--green);color:#fff;font-size:13px;font-weight:600}
.topbar .search{position:absolute;left:128px;top:10px;display:flex;align-items:center;gap:8px}
.topbar .account{position:absolute;right:128px;top:10px;display:flex;gap:10px}

/* hero */
.hero-photo{left:0;top:38px;width:1200px;height:700px;background:linear-gradient(100deg,#f4f6f8 0%,#eef1f4 35%,#dde6ec 60%,#c9d8e3 80%,#e9eef2 100%)}
.header{left:0;top:38px;width:1200px;height:130px}
.logo{position:absolute;left:118px;top:30px;display:flex;align-items:center;gap:12px;font-family:"Fredoka",sans-serif;font-weight:500;font-size:40px;color:var(--pink)}
.logo .mark{width:22px;height:22px;border-radius:50%;background:var(--blue)}
.nav{position:absolute;left:466px;top:46px;display:flex;gap:36px;font-family:"Montserrat",sans-serif;font-size:16px;font-weight:500;color:#333}
.cart{position:absolute;left:1022px;top:40px;width:40px;height:40px;border-radius:50%;background:var(--blue)}
.welcome{left:85px;top:232px;width:364px;height:364px;border-radius:50%;background:#fff;border:6px solid var(--green);padding:8px}
.welcome-inner{width:100%;height:100%;border-radius:50%;background:var(--pink);color:#fff;text-align:center;padding-top:74px}
.welcome h1{font-family:"Montserrat",sans-serif;font-weight:400;font-size:30px;line-height:1.1}
.welcome h1 span{display:block;font-size:40px}
.welcome p{font-size:12.5px;line-height:1.6;margin:12px auto 0;width:230px;opacity:.95}
.btn-outline{display:inline-block;margin-top:18px;padding:10px 30px;border:2px solid #fff;border-radius:24px;font-family:"Montserrat",sans-serif;font-size:15px;font-weight:600}
.dots{left:550px;top:656px;display:flex;gap:6px;align-items:center}
.dots i{width:10px;height:10px;border-radius:50%;background:#fff;display:block;border:2px solid var(--blue)}
.dots b{width:18px;height:18px;border-radius:50%;background:#fff;display:block;border:2px solid #333}

/* categories */
.cat{width:304px;height:304px;border-radius:50%;overflow:hidden;border:12px solid}
.cat .photo{width:100%;height:100%}
.cat .label{position:absolute;left:0;bottom:0;width:100%;height:74px;color:#fff;text-align:center;font-family:"Montserrat",sans-serif;font-weight:600;font-size:23px;padding-top:14px}
.chev{color:#aaa;font-size:44px;line-height:1;font-weight:300}

/* featured */
.section-title{width:1200px;left:0;text-align:center;font-family:"Montserrat",sans-serif;font-weight:500;font-size:32px}
.card{width:230px;background:#fff;border-radius:6px;box-shadow:0 4px 10px rgba(0,0,0,.15);text-align:center;padding:18px 0 20px}
.card .thumb{width:170px;height:150px;margin:0 auto;border-radius:4px}
.card .name{font-family:"Montserrat",sans-serif;font-size:15px;margin-top:16px}
.card .price{font-family:"Montserrat",sans-serif;font-size:21px;font-weight:600}
.btn-pink{display:inline-block;margin-top:8px;background:var(--pink);color:#fff;font-size:12px;font-weight:600;padding:6px 24px;border-radius:16px}
.circle-arrow{width:50px;height:50px;border-radius:50%;border:2px solid #fff;background:var(--blue-dark)}

/* stories */
.story{width:302px;height:340px;background:#fff;box-shadow:0 2px 8px rgba(0,0,0,.12)}
.story .photo{height:190px}
.story .date{position:absolute;left:10px;top:208px;width:54px;height:54px;border-radius:50%;background:var(--green);color:#fff;text-align:center;font-family:"Montserrat",sans-serif;font-size:18px;line-height:1;padding-top:10px}
.story .date small{display:block;font-size:10px;margin-top:2px}
.story h3{position:absolute;left:78px;top:212px;font-family:"Montserrat",sans-serif;font-weight:500;font-size:15px}
.story p{position:absolute;left:78px;top:236px;width:212px;font-size:10.5px;line-height:1.55;color:var(--grey)}
.story .more{position:absolute;left:78px;top:298px;font-size:11px;font-weight:700;color:var(--blue)}

/* testimonials */
.testi-bg{left:0;top:2360px;width:1200px;height:460px;background:linear-gradient(180deg,#fff 0%,#fdf3f6 45%,#f2c9d6 100%)}
.testi-box{left:224px;top:2530px;width:770px;height:226px;border:2px solid var(--blue);border-radius:113px;background:#fff;text-align:center;padding-top:50px}
.testi-box p{font-style:italic;font-size:15px;line-height:1.95;color:#555;width:640px;margin:0 auto}
.testi-box .author{font-family:"Montserrat",sans-serif;font-size:16px;margin-top:14px;color:#222}
.quote-badge{left:578px;top:2510px;width:46px;height:46px;border-radius:50%;background:var(--blue);color:#fff;font-family:Georgia,serif;font-size:42px;text-align:center;line-height:60px;font-weight:700}
.ring-arrow{width:48px;height:48px;border-radius:50%;border:2px solid var(--green);background:#fff}

/* footer */
.footer{left:0;top:2806px;width:1200px;height:384px;background:var(--pink);color:#fff}
.footer .flogo{position:absolute;left:119px;top:140px;font-family:"Fredoka",sans-serif;font-weight:500;font-size:38px;display:flex;align-items:center;gap:12px}
.footer .flogo .mark{width:20px;height:20px;background:#fff;border-radius:50%}
.fcol{position:absolute;top:140px}
.fcol h4{font-family:"Montserrat",sans-serif;font-weight:500;font-size:19px;margin-bottom:14px}
.fcol li{list-style:none;font-size:14px;line-height:26px}
.social{display:flex;gap:14px}
.social i{display:block;width:40px;height:40px;border:2px solid #fff;border-radius:50%}
.cards{display:flex;gap:8px;margin-top:24px}
.cards i{display:block;width:40px;height:24px;background:#fff;border-radius:3px}
.copyright{left:0;top:3190px;width:1200px;height:65px;background:var(--pink-dark);color:#f7c6d2;text-align:center;font-size:13px;line-height:65px}
</style>
</head>
<body>
<div class="page">

  <!-- hero -->
  <div class="abs hero-photo" role="img" aria-label="Photo of a little girl stacking colourful toy blocks in a bright playroom"></div>

  <div class="abs topbar">
    <div class="search">
      <svg width="14" height="14" viewBox="0 0 14 14"><circle cx="6" cy="6" r="4.5" fill="none" stroke="#fff" stroke-width="2"/><line x1="9.5" y1="9.5" x2="13" y2="13" stroke="#fff" stroke-width="2"/></svg>
      Search Product
    </div>
    <div class="account"><span>My Account</span><span>|</span><span>Sign Up</span><span>|</span><span>Wishlist</span><span>|</span><span>Support</span></div>
  </div>

  <header class="abs header">
    <div class="logo"><span class="mark"></span>Bramble-Nook.ca</div>
    <nav class="nav"><span>About Us</span><span>Products</span><span>Girls</span><span>Boys</span><span>Blogs</span><span>Contact</span></nav>
    <div class="cart"><svg width="40" height="40" viewBox="0 0 40 40"><rect x="13" y="16" width="14" height="11" rx="2" fill="#fff"/><path d="M16 16v-2a4 4 0 0 1 8 0v2" fill="none" stroke="#fff" stroke-width="2"/></svg></div>
  </header>

  <div class="abs welcome">
    <div class="welcome-inner">
      <h1>Welcome to<span>Bramble Nook</span></h1>
      <p>Aenatibus et magnis dis parturient montes nascetur ridiculus mus in iaculis facilisis massa Etiam</p>
      <span class="btn-outline">Shop Now</span>
    </div>
  </div>

  <div class="abs dots"><b></b><i></i><i></i><i></i><i></i><b></b></div>

  <svg class="abs" style="left:0;top:590px" width="1200" height="160" viewBox="0 0 1200 160">
    <path d="M0 60 C200 110 420 120 640 80 C860 40 1020 20 1200 40 L1200 160 L0 160Z" fill="var(--green)"/>
    <path d="M0 72 C220 120 440 130 660 92 C880 56 1040 40 1200 58 L1200 160 L0 160Z" fill="var(--pink)"/>
    <path d="M0 96 C240 140 460 142 680 110 C900 78 1050 66 1200 80 L1200 160 L0 160Z" fill="var(--blue)"/>
    <path d="M0 108 C240 150 470 150 690 122 C910 94 1060 86 1200 98 L1200 160 L0 160Z" fill="#fff"/>
  </svg>

  <!-- categories -->
  <div class="abs chev" style="left:80px;top:920px">&#8249;</div>
  <div class="abs chev" style="left:1104px;top:920px">&#8250;</div>

  <div class="abs cat" style="left:102px;top:794px;border-color:var(--blue)">
    <div class="photo" role="img" aria-label="Photo of a child riding a bike outdoors" style="background:linear-gradient(160deg,#cfe0e8,#9fb7a5 60%,#8a8f95)"></div>
    <div class="label" style="background:var(--blue)">Outdoor</div>
  </div>
  <div class="abs cat" style="left:453px;top:794px;border-color:var(--green)">
    <div class="photo" role="img" aria-label="Photo of folded kids' clothing" style="background:linear-gradient(160deg,#e9e3da,#5d7fa6 55%,#d7c3a6)"></div>
    <div class="label" style="background:var(--green)">Clothing</div>
  </div>
  <div class="abs cat" style="left:788px;top:794px;border-color:var(--pink)">
    <div class="photo" role="img" aria-label="Photo of a pile of colourful toys" style="background:linear-gradient(160deg,#e8dccb,#e65b4d 45%,#f2c23a 70%,#4d8ac9)"></div>
    <div class="label" style="background:var(--pink)">Toys</div>
  </div>

  <!-- featured -->
  <svg class="abs" style="left:0;top:1120px" width="1200" height="680" viewBox="0 0 1200 680">
    <path d="M0 40 C300 100 600 110 900 60 C1020 40 1120 20 1200 10 L1200 640 C900 590 700 600 400 650 C250 672 100 670 0 650Z" fill="var(--green)"/>
    <path d="M0 60 C300 116 600 126 900 78 C1020 58 1120 40 1200 30 L1200 620 C900 570 700 580 400 630 C250 652 100 650 0 630Z" fill="var(--blue)"/>
  </svg>
  <h2 class="abs section-title" style="top:1250px;color:#fff">Featured Items</h2>

  <div class="abs circle-arrow" style="left:36px;top:1455px"><svg width="46" height="46" viewBox="0 0 46 46"><path d="M26 15l-8 8 8 8" fill="none" stroke="#fff" stroke-width="2.5"/></svg></div>
  <div class="abs circle-arrow" style="left:1108px;top:1455px"><svg width="46" height="46" viewBox="0 0 46 46"><path d="M20 15l8 8-8 8" fill="none" stroke="#fff" stroke-width="2.5"/></svg></div>

  <div class="abs card" style="left:124px;top:1322px">
    <div class="thumb" role="img" aria-label="Striped kids' sweater" style="background:linear-gradient(180deg,#fff,#d7dbe8 40%,#3b4a7a 70%,#fff)"></div>
    <div class="name">Product Name</div><div class="price">$25.99</div><span class="btn-pink">Buy Now</span>
  </div>
  <div class="abs card" style="left:369px;top:1369px">
    <div class="thumb" role="img" aria-label="Boys' plaid shirt and trousers" style="background:linear-gradient(180deg,#fff,#6e7f95 40%,#b89470 75%,#fff)"></div>
    <div class="name">Product Name</div><div class="price">$25.99</div><span class="btn-pink">Buy Now</span>
  </div>
  <div class="abs card" style="left:616px;top:1322px">
    <div class="thumb" role="img" aria-label="Small red kids' bicycle" style="background:linear-gradient(180deg,#fff,#f1d4d4 45%,#555 75%,#fff)"></div>
    <div class="name">Product Name</div><div class="price">$25.99</div><span class="btn-pink">Buy Now</span>
  </div>
  <div class="abs card" style="left:862px;top:1375px">
    <div class="thumb" role="img" aria-label="Stacking rings toy and teddy bear" style="background:linear-gradient(180deg,#fff,#e94d3c 35%,#f5c73a 60%,#3c8ed0 80%,#fff)"></div>
    <div class="name">Product Name</div><div class="price">$25.99</div><span class="btn-pink">Buy Now</span>
  </div>

  <!-- stories -->
  <div class="abs" style="left:0;top:1790px;width:1200px;height:500px;background:var(--green-soft)"></div>
  <svg class="abs" style="left:0;top:1740px" width="1200" height="90" viewBox="0 0 1200 90">
    <path d="M0 30 C250 0 500 10 700 40 C900 70 1050 70 1200 50 L1200 0 L0 0Z" fill="var(--blue)"/>
    <path d="M0 30 C250 0 500 10 700 40 C900 70 1050 70 1200 50" fill="none" stroke="#fff" stroke-width="4"/>
  </svg>
  <h2 class="abs section-title" style="top:1800px;color:var(--pink)">Mom's Stories</h2>

  <article class="abs story" style="left:126px;top:1873px">
    <div class="photo" role="img" aria-label="Photo of two children riding bikes in a park" style="background:linear-gradient(160deg,#6f9a3c,#9ec25a 50%,#d7588a 80%)"></div>
    <div class="date">01<small>AUG</small></div>
    <h3>Your Blog Title here</h3>
    <p>netus et malesuada fames ac turpis egestas Cras id elit Integer quis urna Ut ante enim dapibus males</p>
    <span class="more">READ MORE</span>
  </article>
  <article class="abs story" style="left:456px;top:1873px">
    <div class="photo" role="img" aria-label="Photo of a child playing among colourful building bricks" style="background:linear-gradient(160deg,#e44a3d,#f3c33c 40%,#3b8ed2 70%,#5ab04b)"></div>
    <div class="date">01<small>AUG</small></div>
    <h3>Your Blog Title here</h3>
    <p>netus et malesuada fames ac turpis egestas Cras id elit Integer quis urna Ut ante enim dapibus males</p>
    <span class="more">READ MORE</span>
  </article>
  <article class="abs story" style="left:785px;top:1873px">
    <div class="photo" role="img" aria-label="Photo of children's clothes on a rack" style="background:linear-gradient(90deg,#2c4e85,#d8504a 35%,#e8c24a 60%,#8c3f8f 85%)"></div>
    <div class="date">01<small>AUG</small></div>
    <h3>Your Blog Title here</h3>
    <p>netus et malesuada fames ac turpis egestas Cras id elit Integer quis urna Ut ante enim dapibus males</p>
    <span class="more">READ MORE</span>
  </article>

  <!-- testimonials -->
  <div class="abs testi-bg" role="img" aria-label="Soft silhouettes of children playing"></div>
  <svg class="abs" style="left:0;top:2240px" width="1200" height="160" viewBox="0 0 1200 160">
    <path d="M0 0 L1200 0 L1200 30 C1000 70 800 110 600 100 C400 90 200 40 0 30Z" fill="var(--green-soft)"/>
    <path d="M0 30 C200 40 400 90 600 100 C800 110 1000 70 1200 30 L1200 60 C1000 100 800 140 600 130 C400 120 200 70 0 60Z" fill="var(--green)"/>
    <path d="M0 60 C200 70 400 120 600 130 C800 140 1000 100 1200 60 L1200 80 C1000 118 800 155 600 146 C400 138 200 90 0 80Z" fill="var(--pink)"/>
    <path d="M0 80 C200 90 400 138 600 146 C800 155 1000 118 1200 80 L1200 96 C1000 132 800 160 600 156 C400 152 200 104 0 96Z" fill="var(--blue)"/>
  </svg>
  <h2 class="abs section-title" style="top:2450px;font-size:29px;font-weight:600;color:#111">Testimonials</h2>

  <div class="abs ring-arrow" style="left:150px;top:2613px"><svg width="44" height="44" viewBox="0 0 44 44"><path d="M25 15l-7 7 7 7" fill="none" stroke="var(--green)" stroke-width="2.5"/></svg></div>
  <div class="abs ring-arrow" style="left:1006px;top:2613px"><svg width="44" height="44" viewBox="0 0 44 44"><path d="M19 15l7 7-7 7" fill="none" stroke="var(--green)" stroke-width="2.5"/></svg></div>

  <div class="abs testi-box">
    <p>penatibus et magnis dis parturient montes nascetur ridiculus mus in iaculis facilisis massa Etiam eu urna Sed porta Suspendisse quam leo molestie sed luctus quis feugiat in pede Fusce tellus Sed metus augue convallis et vehicula ut pulvinar</p>
    <div class="author">By Author Name</div>
  </div>
  <div class="abs quote-badge">&#8220;</div>

  <!-- footer -->
  <footer class="abs footer">
    <svg style="position:absolute;left:0;top:0" width="1200" height="30" viewBox="0 0 1200 30">
      <path d="M0 0 C300 30 900 30 1200 0 L1200 0Z" fill="#f2c9d6"/>
      <path d="M180 10 C500 30 800 28 1060 8" fill="none" stroke="var(--blue)" stroke-width="3"/>
    </svg>
    <div class="flogo"><span class="mark"></span>Bramble-Nook.ca</div>
    <div class="fcol" style="left:462px"><h4>Quick Links</h4><ul><li>Home</li><li>About Us</li><li>Our Products</li><li>Category</li><li>Best Sellers</li></ul></div>
    <div class="fcol" style="left:662px"><h4>Resources</h4><ul><li>My Account</li><li>Wishlist</li><li>My Cart</li><li>Shop Now</li><li>Support</li></ul></div>
    <div class="fcol" style="left:857px"><h4>Follow Us</h4>
      <div class="social"><i></i><i></i></div>
      <div class="cards"><i></i><i></i><i></i><i></i></div>
    </div>
  </footer>
  <div class="abs copyright">© 2018 Company Name &nbsp;All right reserved</div>

</div>
</body>
</html>
```